Truck Wrap for Desk Depot Outlet

We need a professionally designed truck wrap for our 26' box delivery trucks. DDO is a leading provider of new and used office furniture, workspace solutions, and architectural walls in South Florida. We have been in business 35 years. We would like to see designs with a red background on our truck wrap. Our logo is a simple stencil font. The final design should be clean an eye catching.

Target Market(s)

Businesses of all sizes

Industry/Entity Type

Commercial Office Furniture

Font styles to use
Other font styles liked:
• Stencil font for the company logo

Colors

Designer to choose colors to be used in the design.

Requirements
Must have
• Red background CMYK: 0, 90, 91, 6
Should not have
• I don't want the words overly crowded. It must be easy to read.

```html
<!DOCTYPE html>
<html lang="en">
<head>
<meta charset="utf-8">
<title>Desk Depot Outlet – Truck Wrap Panels</title>
<link href="https://fonts.googleapis.com/css2?family=Russo+One&display=swap" rel="stylesheet">
<style>
  :root{
    --brand-red:#f01816;
    --ink:#111111;
    --white:#ffffff;
    --box-white:#eeeeee;
    --charcoal:#333333;
    --backdrop-top:#dde3e7;
    --backdrop-bottom:#b9c4cb;
  }
  html,body{margin:0;padding:0;overflow:hidden;}
  body{
    width:821px;height:1200px;position:relative;
    background:linear-gradient(180deg,var(--backdrop-top),var(--backdrop-bottom));
  }
  .panel{position:absolute;display:block;box-shadow:0 6px 18px rgba(0,0,0,.25);}
  .panel--left-side{left:40px;top:70px;width:741px;height:236px;}
  .panel--front{left:40px;top:482px;width:300px;height:140px;}
  .panel--rear{left:400px;top:380px;width:381px;height:350px;}
  .panel--right-side{left:40px;top:820px;width:741px;height:236px;}

  .display{font-family:'Russo One',sans-serif;}
  .web-address{font-size:20px;fill:var(--white);}
  .web-address--dark{fill:var(--ink);font-size:18px;}
  .selling-point{font-size:22px;fill:var(--white);}
  .selling-point--small{font-size:16px;}
  .phone-line{font-size:26px;fill:var(--white);}
  .phone-line--red{fill:var(--brand-red);font-size:19px;}
  .company-name{font-family:'Russo One',sans-serif;font-size:18px;fill:var(--white);}
  .company-name--dark{fill:var(--charcoal);}
  .band{fill:var(--ink);}
  .band--light{fill:var(--white);}
  .name-square{fill:var(--brand-red);}
  .name-square--outlined{stroke:var(--white);stroke-width:2;}
  .bullet-icon{fill:var(--white);}
</style>
</head>
<body>

<svg width="0" height="0" style="position:absolute" aria-hidden="true">
  <defs>
    <linearGradient id="interior-tone" x1="0" y1="0" x2="1" y2="1">
      <stop offset="0" stop-color="#dd1a24"/>
      <stop offset="0.55" stop-color="#b3121c"/>
      <stop offset="1" stop-color="#7f0b13"/>
    </linearGradient>
  </defs>
</svg>

<!-- Driver side box panel -->
<svg class="panel panel--left-side" viewBox="0 0 741 236">
  <g role="img" aria-label="Red-tinted photograph of a modern office interior with desks and chairs">
    <rect width="741" height="236" fill="url(#interior-tone)"/>
  </g>
  <path class="band" d="M0 46 L392 0 Q386 34 360 40 L0 92 Z"/>
  <text class="display web-address" transform="translate(10 80) rotate(-9)">DESKDEPOTONLINE.COM</text>

  <g class="name-lockup" transform="translate(28 118)">
    <rect class="name-square name-square--outlined" x="0" y="0" width="40" height="40"/>
    <text class="company-name" x="52" y="27">Desk Depot Outlet</text>
  </g>

  <g class="selling-points" transform="translate(290 92) rotate(-8)">
    <path class="bullet-icon" d="M0 -15 L6 -10 L-6 -10Z M0 -3 L6 -8 L-6 -8Z"/>
    <text class="display selling-point" x="12" y="0">Huge Selection</text>
    <path class="bullet-icon" d="M2 16 L-3 21 L2 26Z M6 16 L11 21 L6 26Z"/>
    <text class="display selling-point" x="17" y="29">Everyday Low Prices</text>
    <path class="bullet-icon" d="M8 43 L14 48 L2 48Z M8 55 L14 50 L2 50Z"/>
    <text class="display selling-point" x="22" y="58">Quick Professional Delivery</text>
  </g>

  <path class="band" d="M282 236 Q284 208 310 204 L741 140 L741 236 Z"/>
  <text class="display phone-line" transform="translate(304 228) rotate(-8.6)">954-555-0147 | 305-555-0182</text>
</svg>

<!-- Front box panel (above cab) -->
<svg class="panel panel--front" viewBox="0 0 300 140">
  <g role="img" aria-label="Red-tinted photograph of a modern office interior">
    <rect width="300" height="140" fill="url(#interior-tone)"/>
  </g>
  <g class="name-lockup" transform="translate(30 50)">
    <rect class="name-square name-square--outlined" x="0" y="0" width="36" height="36"/>
    <text class="company-name" x="48" y="25">Desk Depot Outlet</text>
  </g>
</svg>

<!-- Rear door panel -->
<svg class="panel panel--rear" viewBox="0 0 381 350">
  <rect width="381" height="350" fill="var(--box-white)"/>
  <g role="img" aria-label="Red-tinted photograph of an office interior with desks, shelving and chairs">
    <path d="M0 176 L381 70 L381 350 L0 350 Z" fill="url(#interior-tone)"/>
  </g>
  <g class="name-lockup" transform="translate(40 56)">
    <rect class="name-square" x="0" y="0" width="44" height="44"/>
    <text class="company-name company-name--dark" x="56" y="29" font-size="20">Desk Depot Outlet</text>
  </g>

  <path class="band--light" d="M0 184 L356 98 Q346 130 325 136 L0 224 Z"/>
  <text class="display web-address web-address--dark" transform="translate(16 210) rotate(-13)">DESKDEPOTONLINE.COM</text>

  <g class="selling-points" transform="translate(40 250) rotate(-12.5)">
    <path class="bullet-icon" d="M0 -12 L5 -8 L-5 -8Z M0 -2 L5 -6 L-5 -6Z"/>
    <text class="display selling-point selling-point--small" x="10" y="0">Huge Selection</text>
    <path class="bullet-icon" d="M2 12 L-2 16 L2 20Z M6 12 L10 16 L6 20Z"/>
    <text class="display selling-point selling-point--small" x="15" y="22">Everyday Low Prices</text>
    <path class="bullet-icon" d="M8 32 L13 36 L3 36Z M8 42 L13 38 L3 38Z"/>
    <text class="display selling-point selling-point--small" x="20" y="44">Quick Professional Delivery</text>
  </g>

  <path class="band--light" d="M20 350 Q26 320 56 312 L381 236 L381 268 L182 350 Z"/>
  <text class="display phone-line phone-line--red" transform="translate(50 336) rotate(-12.5)">954-555-0147 | 305-555-0182</text>
</svg>

<!-- Passenger side box panel -->
<svg class="panel panel--right-side" viewBox="0 0 741 236">
  <g role="img" aria-label="Red-tinted photograph of a modern office interior with desks and chairs">
    <rect width="741" height="236" fill="url(#interior-tone)"/>
  </g>
  <path class="band" d="M344 0 L741 0 L741 92 L372 40 Q350 36 344 0 Z"/>
  <text class="display web-address" transform="translate(372 22) rotate(8.5)">DESKDEPOTONLINE.COM</text>

  <g class="selling-points" transform="translate(40 50) rotate(7.6)">
    <path class="bullet-icon" d="M0 -16 L6 -11 L-6 -11Z M0 -3 L6 -8 L-6 -8Z"/>
    <text class="display selling-point" x="13" y="0" font-size="24">Huge Selection</text>
    <path class="bullet-icon" d="M-1 18 L-6 23 L-1 28Z M3 18 L8 23 L3 28Z"/>
    <text class="display selling-point" x="13" y="32" font-size="24">Everyday Low Prices</text>
    <path class="bullet-icon" d="M0 50 L6 55 L-6 55Z M0 63 L6 58 L-6 58Z"/>
    <text class="display selling-point" x="13" y="66" font-size="24">Quick Professional Delivery</text>
  </g>

  <path class="band" d="M0 137 L440 205 Q455 210 458 236 L0 236 Z"/>
  <text class="display phone-line" transform="translate(11 166) rotate(8)">954-555-0147 | 305-555-0182</text>

  <g class="name-lockup" transform="translate(488 134)">
    <rect class="name-square name-square--outlined" x="0" y="0" width="40" height="40"/>
    <text class="company-name" x="52" y="27">Desk Depot Outlet</text>
  </g>
</svg>

</body>
</html>
```